Business Card for Pottery and Jewellery Designer

A new business card design is needed to accompany a newly launching pottery and jewellery website. The company logo has been attached for use. The company is called Glazewick Studio. For a sense of the vibe please see the website (it is currently under construction but this way you'll get a feel for the style) www.GlazewickStudio.com

The website font is Pontano Sans for the body of the text with Overlock for headers.

The overall look should be clean and elegant. The back side can have just the logo. The front side should have a smaller logo and the following details displayed:

Glazewick Studio
Designer: Hollis Marrow
Phone: xxx.xxx.xxxx
Email: Designer@GlazewickStudio.com

The structure of displaying this is completely up to you. Different layouts and creative methods of displaying contact info are welcome as long as it stays clean/uncluttered.

No product photographs are to be included in the design as the catalogue changes quickly.

Colour preferences lean towards elegant and understated (charcoal grey, dark navy blue etc.)

Please let me know if you have any further questions or further details required.

Target Market(s)

Target market is 30+ year old women

Industry/Entity Type

Construction

Colors
ffffff
1b1b1b
474747
d9d9d9
fafafa
0355a3

Requirements
Must have
• The submissions so far have looked very typical and don't stand out right now. They're also all in navy with very little variation. I'm looking for something that stands out a it more while still being clean-looking.
Nice to have
• I've attached a few design samples and an idea for a backdrop. It would be great to see some designs in black, white, and grey with only a hint of color.
Should not have
• Product Images

```html
<!DOCTYPE html>
<html lang="en">
<head>
<meta charset="utf-8">
<title>Glazewick Studio — Business Card</title>
<link href="https://fonts.googleapis.com/css2?family=Cinzel:wght@400&family=Lato:wght@400&display=swap" rel="stylesheet">
<style>
  :root {
    --page-bg: #ffffff;
    --label-ink: #1b1b1b;
    --front-bg: #d1d2d4;
    --back-bg: #474546;
    --text-ink: #4a4a4a;
    --icon-fill: #474546;
    --badge-white: #ffffff;
    --brand-navy: #26225e;
    --url-ink: #6b6b6b;
  }
  html, body {
    margin: 0;
    padding: 0;
    width: 1200px;
    height: 998px;
    overflow: hidden;
    background: var(--page-bg);
  }
  .sheet {
    position: relative;
    width: 1200px;
    height: 998px;
    font-family: "Lato", sans-serif;
  }
  .side-label {
    position: absolute;
    top: 60px;
    font-size: 15px;
    color: var(--label-ink);
  }
  .side-label--front { left: 90px; }
  .side-label--back { left: 630px; }

  .card {
    position: absolute;
    width: 471px;
    height: 834px;
  }
  .card--front {
    left: 89px;
    top: 99px;
    background: var(--front-bg);
  }
  .card--back {
    left: 630px;
    top: 97px;
    background: var(--back-bg);
  }

  .contact {
    position: absolute;
    left: 52px;
    top: 48px;
    color: var(--text-ink);
  }
  .contact__role {
    font-size: 17px;
    margin: 0 0 8px;
  }
  .contact__name {
    font-family: "Cinzel", serif;
    font-weight: 400;
    font-size: 34px;
    letter-spacing: 1px;
    margin: 0 0 4px;
    line-height: 1.1;
  }
  .contact__phone {
    font-size: 25px;
    margin: 0 0 6px;
  }
  .contact__email {
    font-size: 21.5px;
    margin: 0;
  }

  .social {
    position: absolute;
    left: 382px;
    top: 602px;
  }

  .badge {
    position: absolute;
    left: 25px;
    top: 205px;
    width: 420px;
    height: 420px;
    border-radius: 50%;
    background: var(--badge-white);
  }
  .brand-name {
    position: absolute;
    left: 0;
    right: 0;
    top: 225px;
    text-align: center;
    font-family: "Cinzel", serif;
    font-weight: 400;
    font-size: 34px;
    letter-spacing: 3px;
    color: var(--brand-navy);
    margin: 0;
  }
  .brand-url {
    position: absolute;
    left: 0;
    right: 0;
    top: 325px;
    text-align: center;
    font-size: 19.5px;
    color: var(--url-ink);
    margin: 0;
  }
</style>
</head>
<body>
<main class="sheet">
  <span class="side-label side-label--front">Front</span>
  <span class="side-label side-label--back">Back</span>

  <section class="card card--front" aria-label="Card front">
    <div class="contact">
      <p class="contact__role">Designer</p>
      <h1 class="contact__name">HOLLIS MARROW</h1>
      <p class="contact__phone">000.000.0000</p>
      <p class="contact__email">Designer@GlazewickStudio.com</p>
    </div>
    <svg class="social" width="40" height="166" viewBox="0 0 40 166" role="img" aria-label="Social media links">
      <circle cx="20" cy="20" r="19" fill="var(--icon-fill)"/>
      <circle cx="20" cy="83" r="19" fill="var(--icon-fill)"/>
      <circle cx="20" cy="146" r="19" fill="var(--icon-fill)"/>
    </svg>
  </section>

  <section class="card card--back" aria-label="Card back">
    <div class="badge">
      <h2 class="brand-name">Glazewick Studio</h2>
      <p class="brand-url">www.GlazewickStudio.com</p>
    </div>
  </section>
</main>
</body>
</html>
```